Business Card Design Project

I have had my current business card for 6years and it is time to upgrade my business card. I have uploaded my old card
I am a retail specialty shop designer and want something designer looking but professional.
Target Market(s)
30-60 year old people in retail businesses
Industry/Entity Type
Retail
Requirements
Must have
- The Vela Fitouts logo (but colour can and style can be altered)
My name, position and contact details as per my existing card attached .
Rupert Calloway Director
m: 0418536771
rupert@velafitouts.com.au
www.velafitouts.com.au
t:02 94417268 f: 02 94417293
po box 817 alexandria nsw 1435
Nice to have
- Use both sides of the card

```html
<!DOCTYPE html>
<html lang="en">
<head>
<meta charset="utf-8">
<title>Vela Fitouts — Business Card</title>
<link rel="stylesheet" href="https://fonts.googleapis.com/css2?family=Open+Sans:wght@400;600;700&display=swap">
<style>
  :root {
    --stage: #2b2b2b;
    --paper-light: #fdf0c6;
    --paper-mid: #f9e3a2;
    --paper-edge: #f1cd72;
    --amber: #efa400;
    --amber-soft: #f3b43a;
    --white: #ffffff;
    --brown: #8a5a12;
    --ink: #6b4608;
  }
  * { margin: 0; padding: 0; box-sizing: border-box; }
  html, body {
    width: 1200px;
    height: 900px;
    overflow: hidden;
    background: var(--stage);
    font-family: "Open Sans", Arial, sans-serif;
  }
  .stage {
    position: relative;
    width: 1200px;
    height: 900px;
    display: flex;
    justify-content: center;
    align-items: center;
    gap: 80px;
  }
  .card {
    position: relative;
    width: 360px;
    height: 620px;
    overflow: hidden;
    background: radial-gradient(ellipse 75% 70% at 50% 45%, var(--paper-light) 0%, var(--paper-mid) 65%, var(--paper-edge) 100%);
    box-shadow: 0 12px 30px rgba(0,0,0,0.45);
  }

  /* Front */
  .front .logo-tab {
    position: absolute;
    left: 76px;
    top: 0;
    width: 166px;
    height: 200px;
    background: var(--amber);
    border-radius: 0 0 10px 10px;
    box-shadow: 0 3px 6px rgba(120,70,0,0.25);
  }
  .front .logo-tab::after {
    content: "";
    position: absolute;
    inset: 0 8px 8px 8px;
    border: 1px dashed rgba(255,255,255,0.35);
    border-top: none;
    border-radius: 0 0 6px 6px;
  }
  .front .brand-name {
    position: absolute;
    left: 18px;
    right: 14px;
    bottom: 24px;
    color: var(--white);
    font-weight: 600;
    font-size: 30px;
    line-height: 1.0;
  }
  .front .web {
    position: absolute;
    left: 76px;
    top: 250px;
    color: var(--brown);
    font-size: 13px;
    letter-spacing: 0.3px;
    text-transform: uppercase;
  }

  /* Back */
  .back .brand-name {
    position: absolute;
    left: 26px;
    top: 30px;
    color: var(--white);
    font-weight: 600;
    font-size: 26px;
    line-height: 1.0;
  }
  .back .contact-band {
    position: absolute;
    left: 0;
    right: 0;
    top: 205px;
    height: 270px;
    background: var(--amber-soft);
    padding: 36px 26px 0 26px;
    color: var(--white);
  }
  .back .person-name {
    font-weight: 700;
    font-size: 22px;
    text-transform: uppercase;
    letter-spacing: 0.2px;
  }
  .back .person-role {
    font-size: 11px;
    color: var(--ink);
    text-transform: uppercase;
  }
  .back .details {
    list-style: none;
    margin-top: 48px;
    font-size: 13px;
    line-height: 1.6;
  }
</style>
</head>
<body>
<main class="stage">
  <section class="card front" aria-label="Business card front">
    <div class="logo-tab">
      <p class="brand-name">Vela<br>Fitouts</p>
    </div>
    <p class="web">www.velafitouts.com.au</p>
  </section>

  <section class="card back" aria-label="Business card back">
    <p class="brand-name">Vela<br>Fitouts</p>
    <div class="contact-band">
      <h1 class="person-name">Rupert Calloway</h1>
      <p class="person-role">Director</p>
      <ul class="details">
        <li>PO Box 817 Kestrel Bay VIC 3941</li>
        <li>m: 0418536771</li>
        <li>t: 02 94417268</li>
        <li>f: 02 94417293</li>
        <li>e: rupert@velafitouts.com.au</li>
        <li>w: www.velafitouts.com.au</li>
      </ul>
    </div>
  </section>
</main>
</body>
</html>
```